Creation of a book cover
Size : 14 x 20,5 cm (+ 5 mm bleed area at the top, bottom and right areas)
The Title is a French sentence which means “The heron dreaming on the cold roof of this empty station”. It’s a surrealistic title which has no link to the story.
AUTHOR : Mathieu Vorlange
TITLE : "Le héron rêvant sur le toit froid de cette gare vide »
PUBLISHER (AT THE BOTTOM OF THE PAGE) : Editions Parvenche
I send a PDF file with the kind of cover we have imagine, but you can propose something different. The glass and the fly can of course be used.

```html
<!DOCTYPE html>
<html lang="fr">
<head>
<meta charset="utf-8">
<title>Le héron rêvant sur le toit froid de cette gare vide — Mathieu Vorlange</title>
<link rel="stylesheet" href="https://fonts.googleapis.com/css2?family=Oswald:wght@500;600&family=Creepster&family=Lato:wght@300&display=swap">
<style>
  :root {
    --page-bg: #d4d5d7;
    --cover-bg: #e4e9f2;
    --author-ink: #1e3b43;
    --title-dark: #6e0b0e;
    --title-bright: #d2101a;
    --band-red: #c8121a;
    --band-dark: #7a0a0e;
    --band-text: #ffffff;
    --publisher-ink: #1a1a1a;
    --art-light: #eef1f5;
    --art-mid: #b9c3c8;
    --art-dark: #5b5146;
  }
  * { margin: 0; padding: 0; box-sizing: border-box; }
  html, body {
    width: 1014px;
    height: 1200px;
    overflow: hidden;
    background: var(--page-bg);
  }
  .book-cover {
    position: absolute;
    left: 124px;
    top: 40px;
    width: 766px;
    height: 1120px;
    background: var(--cover-bg);
    overflow: hidden;
  }
  .author {
    position: absolute;
    top: 52px;
    width: 100%;
    text-align: center;
    font-family: "Oswald", sans-serif;
    font-weight: 600;
    font-size: 44px;
    letter-spacing: 1px;
    color: var(--author-ink);
  }
  .title-main {
    position: absolute;
    top: 188px;
    width: 100%;
    text-align: center;
    font-family: "Creepster", cursive;
    font-size: 168px;
    line-height: 1;
    letter-spacing: 4px;
    background: linear-gradient(90deg, var(--title-dark) 0%, var(--title-bright) 35%, var(--title-bright) 65%, var(--title-dark) 100%);
    -webkit-background-clip: text;
    background-clip: text;
    color: transparent;
  }
  .cover-art {
    position: absolute;
    left: 218px;
    top: 345px;
    width: 340px;
    height: 445px;
    border-radius: 10px;
    background:
      radial-gradient(ellipse 45% 20% at 60% 12%, rgba(91,81,70,0.55), transparent 70%),
      radial-gradient(ellipse 50% 10% at 50% 94%, rgba(60,60,60,0.35), transparent 75%),
      linear-gradient(180deg, var(--art-light) 0%, var(--art-mid) 60%, var(--art-light) 100%);
  }
  .title-band {
    position: absolute;
    left: 0;
    top: 818px;
    width: 766px;
    height: 182px;
  }
  .title-band svg {
    position: absolute;
    inset: 0;
  }
  .subtitle {
    position: absolute;
    inset: 0;
    display: flex;
    flex-direction: column;
    justify-content: center;
    align-items: center;
    font-family: "Oswald", sans-serif;
    font-weight: 500;
    font-size: 60px;
    line-height: 1.15;
    color: var(--band-text);
    text-transform: uppercase;
  }
  .publisher {
    position: absolute;
    top: 1028px;
    width: 100%;
    text-align: center;
    font-family: "Lato", sans-serif;
    font-weight: 300;
    font-size: 46px;
    color: var(--publisher-ink);
  }
</style>
</head>
<body>
  <main class="book-cover">
    <p class="author">MATHIEU VORLANGE</p>
    <h1 class="title-main">LE HÉRON</h1>
    <div class="cover-art" role="img" aria-label="Illustration d’un verre d’eau avec une mouche posée sur le bord"></div>
    <div class="title-band">
      <svg width="766" height="182" viewBox="0 0 766 182" aria-hidden="true">
        <defs>
          <linearGradient id="band-fill" x1="0" x2="1" y1="0" y2="0">
            <stop offset="0" stop-color="var(--band-dark)"/>
            <stop offset="0.2" stop-color="var(--band-red)"/>
            <stop offset="0.8" stop-color="var(--band-red)"/>
            <stop offset="1" stop-color="var(--band-dark)"/>
          </linearGradient>
        </defs>
        <polygon fill="url(#band-fill)" points="0,8 40,4 80,7 120,2 150,6 230,4 300,8 360,3 430,6 500,2 560,7 640,4 700,6 766,3 766,172 720,176 660,171 600,178 540,174 470,179 400,173 330,178 260,174 190,179 120,173 60,178 20,174 0,176"/>
      </svg>
      <h2 class="subtitle"><span>Rêvant sur le toit froid</span><span>de cette gare vide</span></h2>
    </div>
    <p class="publisher">Editions Parvenche</p>
  </main>
</body>
</html>
```